Wine labels Velmora Wine Council - Nueva etiqueta El Consejo Regulador de vinos de Albarrán

Velmora Wines Council, based in southern Spain, are looking to create a new suite of wine labels which retain the elegance of the Velmora Wines industry while reinvigorating their image to the modern era and a new generation of Sherry Wine lovers. These labels will be used across the Velmora Wines Council's range of wines for the promotion of the Velmora Wines industry.

Your design must present at least two styles of Velmora Wines which demonstrate an elegant, modern interpretation and understanding of the unique mood and personality for these wines and the essence of southern Spain.

10 labels will be created based on the winning design, one for each of the unique varieties of Velmora Wines within the collection. This collection comprises of several different wine varieties including: Fino, Manzanilla, Amontillado, Oloroso, Palo Cortado, Medium, Cream, Pale Cream, Pedro Ximenez and Moscatel.

We recommend you visit our website www.velmora-vinos.example/wines as the source to understanding the origins and unique personality of these diverse wines.

El Consejo Regulador de los Vinos de Albarrán y Tordesal quiere renovar las etiquetas de los vinos utilizados para sus actividades de promoción genérica. Esta colección de vinos comprende las tipologías más importantes de la región que incluye: fino, manzanilla, amontillado, oloroso, palo cortado, pale cream, medium, cream, pedro ximénez y moscatel. Por lo tanto se precisan 10 etiquetas, una para cada uno de los vinos mencionados.
Updates

Project Deadline Extended
Reason: Due to some confusion with the deadline we wish to officially extend the deadline to allow designers one last week to submit their entries.

Target Market(s)

Industry, journalists, media, sommeliers, chefs, wine writers

Industry/Entity Type

Council

Requirements
Must have
• Front and Back label plus capsule:
• Front label can have either of the two official logos of the Velmora Wine council titled Vinos de Albarrán Digital or not, this is optional. Must include: Vino selecionado por el Consejo Regulador de la Denominacion de Origen, Name of the variety of wine eg FINO, percentage of alcohol eg 15% and quantity 75 cl.
• The back of the label must include the council logo titled Sellora and 4 additional logos positioned smaller. The Europa logo must appear larger than the 3 other logos. Space for descriptive text about the wine is also required.
• The dimensions of the bottle can be found at this link http://www.vidrialto.example/es/catalogo/vinos-y-espumosos/bordelesas/bd-orla
• Altura:305 mm
• Diámetro base:76,20 mm
• Diámetro hombro:82 mm
• Tipo boca:Cetie
• Peso:750 gr
• Capacidad:75 cl
• Etiqueta delantera y trasera y capsula
• La etiqueta delantera puede incluir el logo oficial del Consejo Regulador o el logo digital, o ninguno, esto es opcional. Debe incluir el siguiete texto: Vino selecionado por el Consejo Regulador de la Denominacion de Origen, el nombre de la variedad del vino, por ejemplo Fino, el porcentaje de alcohol, por ejemplo 15%, y la capacidad 75cl.
• La etiqueta trasera debe incluir el logo oficial Sellora del Consejo, y cuatro logos adicionales con una dimension menor. El Logo de ¨Europa invierte en las zonas rurales¨ debe ser de mayor tamaño que los otros. Se precisa espacio para el texto descriptivo de los vinos.
• Las dimensiones de la botella se puede encontrar en este enlace
• http://www.vidrialto.example/es/catalogo/vinos-y-espumosos/bordelesas/bd-orla
• Altura:305 mm
• Diámetro base:76,20 mm
• Diámetro hombro:82 mm
• Tipo boca:Cetie
• Peso:750 gr
• Capacidad:75 cl
Nice to have
• See our website velmora-vinos.example to understand the origin of the wines. Ver nuestra página web velmora-vinos.example para mejor entender los vinos.
Should not have
• Images of catavinos or stereotypical images from Spain such as flamenco dancers or guitars.

```html
<!DOCTYPE html>
<html lang="es">
<head>
<meta charset="utf-8">
<title>Etiquetas Vinos de Albarrán</title>
<link href="https://fonts.googleapis.com/css2?family=Cormorant+Garamond:wght@500&family=Questrial&family=Montserrat:wght@400;600&display=swap" rel="stylesheet">
<style>
  :root {
    --bg: #f4efe4;
    --paper: #ffffff;
    --ink: #2b2522;
    --ink-soft: #4a423d;
    --fino: #d4ad2a;
    --fino-wash: #f3e79e;
    --fino-stain: #f1e3a2;
    --amontillado: #7a2d2a;
    --amontillado-stain: #e6cdd6;
  }
  * { margin: 0; padding: 0; box-sizing: border-box; }
  html, body { width: 1200px; height: 906px; overflow: hidden; }
  body {
    background: var(--bg);
    position: relative;
    font-family: "Montserrat", sans-serif;
    color: var(--ink);
  }
  .label {
    position: absolute;
    top: 173px;
    width: 250px;
    height: 560px;
    background: var(--paper);
    box-shadow: 0 2px 10px rgba(60, 45, 30, 0.12);
    text-align: center;
  }
  .label > * { position: absolute; left: 0; right: 0; }
  .label--fino {
    left: 229px;
    background: linear-gradient(to bottom, var(--paper) 0%, var(--paper) 64%, var(--fino-wash) 100%);
  }
  .label--amontillado { left: 703px; }

  .brand { top: 40px; display: flex; flex-direction: column; align-items: center; }
  .brand__mark {
    width: 22px;
    height: 22px;
    border-radius: 50%;
    background: var(--ink);
    margin-bottom: 52px;
  }
  .brand__name {
    font-family: "Cormorant Garamond", serif;
    font-weight: 500;
    font-size: 13px;
    letter-spacing: 0.2px;
    line-height: 1;
  }
  .brand__sub {
    font-size: 5px;
    letter-spacing: 1.4px;
    margin-top: 3px;
  }

  .stain {
    top: 196px;
    left: 64px;
    right: auto;
    width: 122px;
    height: 130px;
  }
  .stain--fino { background: var(--fino-stain); }
  .stain--amontillado { background: var(--amontillado-stain); }

  .variety {
    font-family: "Questrial", sans-serif;
    font-weight: 400;
    line-height: 1;
  }
  .variety--fino { top: 384px; font-size: 50px; color: var(--fino); letter-spacing: 1px; }
  .variety--amontillado { top: 395px; font-size: 30px; color: var(--amontillado); }

  .origin {
    top: 446px;
    font-size: 7.5px;
    line-height: 1.45;
    color: var(--ink-soft);
  }
  .origin strong { font-weight: 600; color: var(--ink); }
  .vintage { top: 491px; font-size: 8px; letter-spacing: 1px; }
  .specs {
    top: 513px;
    display: flex;
    justify-content: center;
    align-items: center;
    gap: 6px;
    font-size: 6.5px;
  }
  .specs__divider { width: 1px; height: 18px; background: var(--ink); }
</style>
</head>
<body>
  <section class="label label--fino">
    <div class="brand">
      <span class="brand__mark" aria-hidden="true"></span>
      <p class="brand__name">VINOS DE ALBARRÁN</p>
      <p class="brand__sub">VELMORA WINES</p>
    </div>
    <div class="stain stain--fino" role="img" aria-label="Ilustración de una mancha circular de vino fino en tono dorado"></div>
    <h2 class="variety variety--fino">FINO</h2>
    <p class="origin">Vino seleccionado por el<br><strong>Consejo Regulador</strong><br>de la Denominación de Origen</p>
    <p class="vintage">2016</p>
    <div class="specs"><span>75 cl</span><span class="specs__divider"></span><span>alc 15%</span></div>
  </section>

  <section class="label label--amontillado">
    <div class="brand">
      <span class="brand__mark" aria-hidden="true"></span>
      <p class="brand__name">VINOS DE ALBARRÁN</p>
      <p class="brand__sub">VELMORA WINES</p>
    </div>
    <div class="stain stain--amontillado" role="img" aria-label="Ilustración de una mancha circular de vino amontillado en tono granate"></div>
    <h2 class="variety variety--amontillado">AMONTILLADO</h2>
    <p class="origin">Vino seleccionado por el<br><strong>Consejo Regulador</strong><br>de la Denominación de Origen</p>
    <p class="vintage">2016</p>
    <div class="specs"><span>75 cl</span><span class="specs__divider"></span><span>alc 15%</span></div>
  </section>
</body>
</html>
```